Infographic Design for Aluminium Can Recycling

We require a neat design that can be integrated into print advertising for a 'cash for cans' recycling promotion and also scaled back for Facebook promotion. The promotion is aimed at kids/families. Needs to be fresh and colourful - but also appealing to children. The flyer is to be designed at A5 size and also at FB post sizing. You can just submit the one design in A5 to win, with the knowledge that you will need to redesign slightly later to suit FB post size.

The design needs to contain as much of the following as possible.

- The best thing is - Aluminium is 100% recyclable FOREVER
- If you recycled just one can everyday for a week, you'd save enough energy to watch TV straight for 21 hours - thats an entire season of XXX
- 105,784 cans are recycled every minute
- it takes the same amount of energy to make 1 new can as it does to recycle 20
- a recycled can is back on the shelf in 60 days
-2/3 of the aluminium ever produced is still in use today

Please keep colours muted - not bright
Please do not present anything like the 'Tidy Loop' lie attached. This is far too busy.
I have attached the original flyer for information only (see below for what to and what NOT to include)
I've attached some cute graphics I think kids and adults will find appealing. Design something similar. The prize to be won is an electric scooter - perhaps they could be riding this.

They are giving away an electric Scooter (not Bike)

Please use Pellbrook Alloy Traders and LOGO

Please provide address and details of event as per flyer

Please leave out the following text:
HEY KIDS
WIN THIS BIKE
FIND US ON FB
LUCKY DOOR PRIZE + SAUSAGE SIZZLE
WE PAY CASH FOR CANS
Collect as many aluminium cans as you can and bring them to our can day and get paid for cash
Do not include the can man graphic

Please have information:
Event location
Win an Electric Scooter
Turn in your CANS for CASH

Great - can't wait to see what you creative geniuses come back with!!
Updates

None of these designs matched the brief. Im actually not sure what to do now?

Target Market(s)

Males 35+

Industry/Entity Type

Advertising

Font styles to use
Sans Serif

Colors
5c5c5c
0555a3
3276b5
b1b1b1
faa54b
fbf289
33a6d7
f04a50

Requirements
Must have
• Please read brief
Nice to have
• Please see brief
Should not have
• Please see brief

```html
<!DOCTYPE html>
<html lang="en">
<head>
<meta charset="utf-8">
<title>Win an Electric Scooter – Cash for Cans</title>
<link rel="stylesheet" href="https://fonts.googleapis.com/css2?family=Arimo:wght@400;700&family=PT+Sans:wght@400&family=Tinos&display=swap">
<style>
  :root{
    --navy:#1a2466;
    --royal:#0555a3;
    --mid-blue:#3276b5;
    --sky:#33a6d7;
    --red:#f04a50;
    --orange:#faa54b;
    --lemon:#fbf289;
    --panel-yellow:#fbf6b8;
    --grey:#5c5c5c;
    --light-grey:#b1b1b1;
    --green:#7db83a;
    --white:#ffffff;
  }
  *{margin:0;padding:0;box-sizing:border-box}
  html,body{width:838px;height:1200px;overflow:hidden;background:var(--white)}
  .flyer{position:relative;width:838px;height:1200px;overflow:hidden;background:var(--white);font-family:"Arimo",sans-serif}
  .hero{position:absolute;left:0;top:0;width:838px;height:665px;
    background:linear-gradient(100deg,var(--navy) 0%,#23409a 40%,#3a7fc4 75%,#1e3684 100%)}
  .tagline{position:absolute;right:62px;top:20px;color:var(--green);font:400 20px "Arimo",sans-serif}
  .banner{position:absolute;left:0;top:0}
  .event{position:absolute;left:34px;top:180px;color:var(--white)}
  .event-row{position:absolute;white-space:nowrap}
  .event-label{position:absolute;left:0;font:400 22px "PT Sans",sans-serif}
  .event-value{position:absolute;left:89px;font:400 35px "PT Sans",sans-serif;line-height:1}
  .prize-box{position:absolute;left:440px;top:266px;width:330px;height:386px;background:var(--white);
    border:1px solid var(--light-grey)}
  .prize-note{position:absolute;left:0;right:0;bottom:10px;text-align:center;font:400 19px "Arimo",sans-serif;color:#111}
  .brand{position:absolute;left:250px;top:515px;width:150px;color:var(--white);
    font:700 21px/1.15 "Arimo",sans-serif;text-align:center;display:flex;flex-direction:column;align-items:center;gap:10px}
  .brand-mark{width:40px;height:40px;background:var(--white)}
  .mascot{position:absolute;left:30px;top:492px;width:165px;height:208px;border-radius:70px 70px 24px 24px;
    background:linear-gradient(180deg,#f3c86a 0%,#f2c9a0 45%,#7ac143 75%,#f28c28 100%);z-index:3}
  .side-tab{position:absolute;left:0;top:667px;width:115px;height:474px;background:var(--royal)}
  .side-tab-text{position:absolute;left:57px;top:252px;transform:translate(-50%,-50%) rotate(-90deg);
    white-space:nowrap;color:var(--white);font:400 38px/1.15 "Tinos",serif;text-align:left}
  .facts-panel{position:absolute;left:123px;top:677px;width:686px;height:464px;background:var(--panel-yellow);
    border-radius:0 0 26px 26px;box-shadow:8px 10px 12px rgba(0,0,0,.35)}
  .fact{position:absolute;padding:22px 20px;font:400 23px/1.4 "Arimo",sans-serif;
    box-shadow:4px 5px 6px rgba(0,0,0,.3)}
  .fact--recyclable{left:172px;top:674px;width:285px;height:123px;background:var(--sky);color:var(--lemon)}
  .fact--per-minute{left:172px;top:810px;width:285px;height:109px;background:var(--mid-blue);color:var(--white);padding-top:14px;line-height:1.35}
  .fact--energy{left:172px;top:933px;width:285px;height:186px;background:var(--royal);color:var(--lemon)}
  .fact--in-use{left:474px;top:677px;width:303px;height:174px;background:var(--red);color:var(--lemon)}
  .fact--tv{left:474px;top:889px;width:313px;height:222px;background:var(--orange);color:var(--royal);padding-top:16px}
  .element-tile{position:absolute;right:24px;top:14px;width:72px;height:76px;border-radius:8px;
    background:linear-gradient(135deg,#d9d9d9,#8d8d8d)}
  .pin{position:absolute;right:14px;top:10px;width:30px;height:30px}
</style>
</head>
<body>
<main class="flyer">
  <section class="hero">
    <p class="tagline">CA$H for CANS</p>
    <svg class="banner" width="838" height="200" viewBox="0 0 838 200">
      <defs>
        <linearGradient id="ribbon" x1="0" y1="0" x2="1" y2="0">
          <stop offset="0" stop-color="#4f9a2e"/>
          <stop offset=".5" stop-color="#8cc63f"/>
          <stop offset="1" stop-color="#5ea635"/>
        </linearGradient>
      </defs>
      <polygon points="60,16 772,64 746,120 772,178 60,104" fill="url(#ribbon)"/>
      <line x1="72" y1="95" x2="82" y2="28" stroke="#ffffff" stroke-width="4" stroke-linecap="round"/>
      <text x="100" y="86" transform="rotate(6 100 86)" fill="#ffffff" stroke="#1a2466" stroke-width="1.5"
        font-family="Arimo, sans-serif" font-weight="700" font-size="58" textLength="610" lengthAdjust="spacingAndGlyphs">Win an Electric Scooter!</text>
    </svg>

    <div class="event">
      <div class="event-row" style="top:12px"><span class="event-label" style="top:6px">When:</span><span class="event-value">Saturday 25th October</span></div>
      <div class="event-row" style="top:70px"><span class="event-label" style="top:6px">Where:</span><span class="event-value">18 Harrowgate St</span></div>
      <div class="event-row" style="top:110px"><span class="event-value">West Corlan</span></div>
      <div class="event-row" style="top:162px"><span class="event-label" style="top:8px">Time:</span><span class="event-value">8am - 12 pm</span></div>
      <div class="event-row" style="top:214px"><span class="event-label" style="top:6px">Phone:</span><span class="event-value">02 4811 2790 or</span></div>
      <div class="event-row" style="top:264px"><span class="event-value">1 300 418 552</span></div>
    </div>

    <div class="prize-box">
      <p class="prize-note">Prize will be Drawn at Noon</p>
    </div>

    <div class="brand">
      <span class="brand-mark"></span>
      <span>Pellbrook Alloy Traders</span>
    </div>
  </section>

  <div class="mascot" role="img" aria-label="Cartoon boy with glasses and a green shirt, waving"></div>

  <aside class="side-tab">
    <p class="side-tab-text">Turn Your Cans into<br>Ca$h!</p>
  </aside>

  <section class="facts-panel" aria-label="Aluminium recycling facts"></section>

  <article class="fact fact--recyclable">Aluminum is<br>100%<br>Recycable
    <div class="element-tile" role="img" aria-label="Aluminium element tile icon"></div>
  </article>
  <article class="fact fact--per-minute">105,784 cans are<br>Recycled<br>every minute
    <svg class="pin" viewBox="0 0 30 30"><polygon points="4,6 26,4 18,26" fill="#b1b1b1" stroke="#5c5c5c" stroke-width="1.5"/></svg>
  </article>
  <article class="fact fact--energy">To make<br>1 New Can =<br>the same amount<br>of energy to<br>recycle 20 cans
    <svg class="pin" viewBox="0 0 30 30"><polygon points="4,6 26,4 18,26" fill="#b1b1b1" stroke="#5c5c5c" stroke-width="1.5"/></svg>
  </article>
  <article class="fact fact--in-use">2/3 of Aluminum<br>ever produced<br>is still in use<br>TODAY
    <svg class="pin" viewBox="0 0 30 30"><polygon points="4,6 26,4 18,26" fill="#b1b1b1" stroke="#5c5c5c" stroke-width="1.5"/></svg>
  </article>
  <article class="fact fact--tv">Recycling just<br>1 can every day<br>for a week<br>will save enough<br>energy to watch<br>21 hrs of TV.
    <svg class="pin" viewBox="0 0 30 30"><polygon points="4,6 26,4 18,26" fill="#b1b1b1" stroke="#5c5c5c" stroke-width="1.5"/></svg>
  </article>
</main>
</body>
</html>
```